Stonelynk Business Card Design

The Stonelynk Co is an aggregate (crushing) equipment dealer serving Western Canadian provinces. Stonelynk is a distributor of aggregate equipment for different manufacturers.

We are looking to change and update the existing business card which has been used since the existence of the company. A copy of existing card has been attached for reference. The Stonelynk Co logo we want to remain the same and we want the green color to remain the same.

We are wanting something new with a different look. A refreshing card to show a new modern and updated look. No longer wanting to have the manufacturers on the back of the card but something more like our logo on the back of the card with a statement like "Crushing Solutions"

ideas could be:
- card can be different colors on front and back
- front or reverse of the card could possibly be the green color with the logo in black

Target Market(s)

Owners of Aggregate/Crushing companies

Requirements
Must have
• - logo to remain same along with same font within logo
• - green color to remain same
Nice to have
• as noted above under project description
Should not have

```html
<!DOCTYPE html>
<html lang="en">
<head>
<meta charset="utf-8">
<title>Stonelynk Business Card</title>
<link rel="stylesheet" href="https://fonts.googleapis.com/css2?family=Arimo:wght@400;700&family=Poppins:wght@600&family=Roboto+Condensed:wght@700&display=swap">
<style>
  :root {
    --page-bg: #e4e5e8;
    --olive-dark: #6b6812;
    --olive-light: #9a9925;
    --olive-line: #7a7616;
    --ink: #111111;
    --paper: #ffffff;
    --band: #0c0c0c;
    --band-text: #f6eef0;
  }
  * { margin: 0; padding: 0; box-sizing: border-box; }
  html, body { width: 1200px; height: 1000px; overflow: hidden; }
  body { background: var(--page-bg); position: relative; font-family: "Arimo", Arial, sans-serif; }

  .card { position: absolute; left: 305px; width: 590px; height: 336px; overflow: hidden; }

  /* Front */
  .card-front {
    top: 121px;
    background: radial-gradient(ellipse at 85% 10%, var(--olive-light), var(--olive-dark) 75%);
    color: var(--paper);
  }
  .brand-name {
    position: absolute; left: 0; right: 0; top: 150px;
    text-align: center;
    font-family: "Poppins", sans-serif; font-weight: 600;
    font-size: 52px; letter-spacing: 4px; line-height: 1;
  }
  .front-contact {
    position: absolute; left: 0; right: 0; top: 294px;
    text-align: center; font-weight: 700; font-size: 12.5px; line-height: 17px; letter-spacing: 0.3px;
  }

  /* Back */
  .card-back { top: 542px; background: var(--paper); color: var(--ink); }
  .holder-name {
    position: absolute; left: 78px; top: 120px;
    font-family: "Poppins", sans-serif; font-weight: 600; font-size: 43px; line-height: 1; letter-spacing: 1px;
  }
  .name-rule { position: absolute; left: 92px; top: 168px; width: 310px; height: 3px; background: var(--olive-line); }
  .holder-email { position: absolute; left: 92px; width: 310px; top: 176px; text-align: center; font-size: 18px; }
  .holder-direct { position: absolute; left: 92px; width: 310px; top: 200px; text-align: center; font-weight: 700; font-size: 12px; }

  .product-lines {
    position: absolute; left: 51px; top: 288px; display: flex; align-items: center;
    font-family: "Roboto Condensed", sans-serif; font-weight: 700; font-size: 23px; letter-spacing: 1.6px;
  }
  .product-lines .divider { display: inline-block; width: 2px; height: 30px; background: var(--olive-line); margin: 0 14px; }

  .address {
    position: absolute; left: 496px; top: 28px; height: 285px;
    writing-mode: vertical-rl; transform: rotate(180deg);
    text-align: center;
    font-family: "Roboto Condensed", sans-serif; font-weight: 700; font-size: 12.5px; letter-spacing: 1px;
    color: var(--olive-line);
  }
  .company-band { position: absolute; right: 0; top: 0; width: 75px; height: 100%; background: var(--band); }
  .company-band span {
    position: absolute; left: 22px; top: 14px; height: 305px;
    writing-mode: vertical-rl; transform: rotate(180deg); text-align: center;
    font-family: "Roboto Condensed", sans-serif; font-weight: 700; font-size: 27px; letter-spacing: 1.5px;
    color: var(--band-text);
  }
</style>
</head>
<body>
  <section class="card card-front">
    <div class="brand-name">STONELYNK</div>
    <div class="front-contact">
      <div>www.STONELYNK.ca</div>
      <div>Tel.: 780.555.0142 / Fax: 780.555.0187</div>
    </div>
  </section>

  <section class="card card-back">
    <div class="holder-name">DALE MORROW</div>
    <div class="name-rule"></div>
    <div class="holder-email">dale@stonelynk.com</div>
    <div class="holder-direct">Direct: 780.555.0163</div>

    <div class="product-lines">
      <span>SCREENERS</span><span class="divider"></span><span>CRUSHERS</span><span class="divider"></span><span>STACKERS</span>
    </div>

    <div class="address">2215 - 48B AVENUE, NISKU, ALBERTA T4X 1K7</div>
    <div class="company-band"><span>THE STONELYNK CO.</span></div>
  </section>
</body>
</html>
```